Bellcroft construction website for a high end luxury custom home builder

I need a website designed for a high end luxury custom home builder. I would like the website to host a number activities. A blog/vlog on the page where I can post about the projects being built how to's what to look out for during the build, A designated testimonial page but also having testimonials posted on the other pages like the gallery linked to the photos of the completed projects. a gallery page, an about us page, services page that demonstrate what we do and what we are capable of, and hopefully when I start winning awards, and awards page.
Home page
about us page
services page
gallery
testimonial
awards page but I my need to add that later.
I already have the domain name for the website. www.bellcroftconstruction.com.au
I recently completed a sketch hive page for my logo and will post the logo documents below.

Target Market(s)

I'd like to target professions with cash enough to build a house. I would like peolpe to understand that they are buy a price when they are getting quote to build there house. It seems like people just look for the cheapest price and end up with an inferior product. Where as people need to understand that a builder with the high price ( not astronomically higher 15-20% higher) are the ones with correct systems in place, a bide by correct OHS and use proper and correct product. If that can be conveyed through the website somehow, without saying it directly, it would be awesome.

Industry/Entity Type

Residential Construction

Coding

Coded - Design and coding required

Number of Pages Required

5+ page

Font styles to use
Sans Serif

Requirements
Must have
• I would like the testimonials to have a designated page (mentioned in the brief) but I would like the testimonials to be linked to the gallery page and when the picture are open of completed job the relevant testimonials would pop up near the pictures.

Nice to have
• I would like peolpe to understand that they are buy a price when they are getting quote to build there house. It seems like people just look for the cheapest price and end up with an inferior product. Where as people need to understand that a builder with the high price ( not astronomically higher 15-20% higher) are the ones with correct systems in place, a bide by correct OHS and use proper and correct product. If that can be conveyed through the website somehow, without saying it directly, it would be awesome.

```html
<!DOCTYPE html>
<html lang="en">
<head>
<meta charset="utf-8">
<title>Bellcroft Construction — High End Luxury Custom Home Builder</title>
<link href="https://fonts.googleapis.com/css2?family=Cinzel:wght@700&family=Oswald:wght@500&family=Poppins:ital,wght@0,400;0,600;1,400&display=swap" rel="stylesheet">
<style>
:root{
  --blue:#1a73c6;
  --blue-dark:#0f5ea8;
  --navy:#0d1f3c;
  --ink:#222;
  --muted:#555;
  --panel:#f2f3f7;
  --white:#fff;
}
*{margin:0;padding:0;box-sizing:border-box}
html,body{width:1200px;height:4164px;overflow:hidden;background:var(--white)}
body{position:relative;font-family:'Poppins',sans-serif;color:var(--ink)}
.abs{position:absolute}
.serif{font-family:'Cinzel',serif;font-weight:700;color:var(--blue)}
.btn{position:absolute;display:flex;align-items:center;justify-content:center;border-radius:22px;background:var(--blue);color:#fff;font-family:'Cinzel',serif;font-weight:700;font-size:14px;letter-spacing:1px}
.photo{position:absolute}

/* header */
.site-header{position:absolute;left:0;top:0;width:1200px;height:75px;background:#fff}
.brand{position:absolute;display:flex;align-items:center;gap:8px}
.brand-mark{width:22px;height:22px;background:var(--blue)}
.brand-name{font-family:'Cinzel',serif;font-weight:700;color:var(--blue);font-size:22px;line-height:1}
.main-nav{position:absolute;left:441px;top:29px;display:flex;gap:20px;font-size:12px;color:#333}
.main-nav .active{color:var(--blue);position:relative}
.main-nav .active::after{content:"";position:absolute;left:50%;top:22px;width:4px;height:4px;margin-left:-2px;border-radius:50%;background:var(--blue)}
.phone-btn{left:873px;top:19px;width:165px;height:36px;font-size:17px;letter-spacing:0;justify-content:flex-start;padding-left:6px;gap:10px}
.phone-btn .ico{width:26px;height:26px;border-radius:50%;background:#fff;display:flex;align-items:center;justify-content:center}

/* hero */
.hero{left:0;top:75px;width:1200px;height:637px;
  background:
    radial-gradient(ellipse 260px 200px at 420px 400px,rgba(232,196,140,.45),transparent 70%),
    radial-gradient(ellipse 380px 160px at 900px 520px,rgba(200,170,120,.25),transparent 70%),
    linear-gradient(180deg,#0a1834 0%,#14284a 40%,#2a3850 70%,#1c2230 100%)}
.hero-title{left:755px;top:318px;font-family:'Oswald',sans-serif;font-size:50px;line-height:52px;color:#fff}
.hero-btn{left:754px;top:497px;width:156px;height:40px}
.hero-dots{left:1113px;top:330px;display:flex;flex-direction:column;gap:13px}
.hero-dots span{width:12px;height:12px;border-radius:50%;background:#3d8fdc}

/* about */
.about{left:0;top:712px;width:1200px;height:564px;background:var(--panel)}
.about-photo{left:600px;top:713px;width:600px;height:563px;
  background:
    linear-gradient(180deg,transparent 84%,#2f86d8 84%,#1c5fa8 100%),
    linear-gradient(170deg,#a9c7e6 0%,#d9e4ee 30%,#7b8da4 48%,#2a3a58 62%,#1a2744 100%)}
.about-card{left:0;top:787px;width:770px;height:413px;background:var(--panel)}
.about-title{left:275px;top:832px;font-size:44px;line-height:52px}
.about-sub{left:275px;top:884px;font-weight:600;font-size:16px;letter-spacing:1.5px;color:#222}
.about-text{left:275px;top:925px;width:400px;font-size:11.5px;line-height:21px;color:var(--muted)}
.about-text p+p{margin-top:12px}
.about-btn{left:272px;top:1109px;width:158px;height:41px}
.play{left:928px;top:996px;width:64px;height:64px;border-radius:50%;background:#fff;border:4px solid var(--blue)}

/* testimonial */
.quote{left:300px;top:1350px;width:600px;text-align:center;font-style:italic;font-size:15.5px;line-height:26px;color:#333}
.quote-mark{left:580px;top:1452px;width:40px;text-align:center;font-family:'Cinzel',serif;font-size:46px;line-height:40px;color:var(--blue)}
.client{left:500px;top:1497px;width:200px;text-align:center;font-family:'Cinzel',serif;font-weight:700;font-size:15px;color:#222}

/* services */
.services{left:0;top:1590px;width:1200px;height:714px;background:var(--panel)}
.section-title{left:0;width:1200px;text-align:center;font-size:44px;line-height:50px}
.section-sub{left:0;width:1200px;text-align:center;font-weight:600;font-size:16px;letter-spacing:1.5px;color:#222}
.services-text{left:0;top:1750px;width:1200px;text-align:center;font-size:12px;line-height:21px;color:var(--muted)}
.services-text em{display:block;margin-top:10px;font-size:13px;color:#333}
.card{position:absolute;top:1864px;width:248px;height:361px;background:#fff;text-align:center}
.card .img{height:262px}
.card h3{margin-top:22px;font-family:'Cinzel',serif;font-size:16px;color:#222;letter-spacing:1px}
.card p{font-size:11px;color:var(--muted);margin-top:2px}
.card i{display:block;width:24px;height:2px;background:var(--blue);margin:10px auto 0}
.card.featured{background:var(--blue)}
.card.featured h3,.card.featured p{color:#fff}
.card.featured i{background:#fff}

/* blog */
.blog-title{left:199px;top:2408px;font-size:44px;line-height:52px}
.blog-sub{left:199px;top:2492px;width:370px;font-family:'Cinzel',serif;font-weight:700;font-size:14.5px;line-height:23px;color:#222}
.blog-text{left:199px;top:2548px;width:350px;font-size:11.5px;line-height:21px;color:var(--muted)}
.blog-btn{left:199px;top:2647px;width:157px;height:40px}
.blog-photo{left:690px;top:2379px;width:510px;height:375px;
  background:
    radial-gradient(ellipse 140px 110px at 330px 120px,rgba(255,255,255,.55),transparent 70%),
    linear-gradient(180deg,#e6e0d4 0%,#d2c9b8 45%,#bdb5a6 62%,#a29a8c 100%)}
.arrows{left:656px;top:2718px;display:flex}
.arrows span{width:34px;height:34px;background:var(--blue);display:flex;align-items:center;justify-content:center}
.arrows span+span{background:var(--blue-dark);border-left:1px solid #5b9ad6}

/* gallery */
.tile{position:absolute}
.tile-overlay{left:0;top:2948px;width:503px;height:239px;background:rgba(26,115,198,.8)}
.tile-frame{left:16px;top:2965px;width:470px;height:205px;border:1px solid rgba(255,255,255,.6)}
.tile-label{left:0;top:3095px;width:503px;text-align:center;font-family:'Cinzel',serif;font-weight:700;font-size:14px;color:#fff;letter-spacing:1px}
.explore-btn{left:517px;top:3460px;width:165px;height:38px}

/* call to action */
.cta{left:0;top:3587px;width:1200px;height:315px;background:var(--blue)}
.cta-house{left:215px;top:3536px;width:380px;height:366px;
  background:linear-gradient(180deg,#f6f7f8 0%,#e4e8ec 50%,#b9c2c4 68%,#6f8a5a 86%,#3f5a34 100%)}
.cta-title{left:632px;top:3660px;font-family:'Cinzel',serif;font-weight:700;font-size:36px;line-height:42px;color:#fff;letter-spacing:1px}
.cta-text{left:632px;top:3746px;font-size:13px;color:#fff}
.cta-btn{left:631px;top:3784px;width:157px;height:40px;background:transparent;border:2px solid #fff}

/* footer */
.footer-brand{left:162px;top:3966px}
.socials{left:162px;top:4019px;display:flex;gap:8px}
.socials span{width:29px;height:29px;border-radius:50%;background:var(--blue)}
.copyright{left:162px;top:4064px;width:210px;font-size:10px;line-height:17px;color:var(--muted)}
.f-col{position:absolute;top:3943px}
.f-col h4{font-family:'Cinzel',serif;font-weight:700;font-size:15px;color:var(--blue);letter-spacing:.5px;margin-bottom:14px}
.f-col li{list-style:none;font-size:10.5px;line-height:19.5px;color:var(--muted)}
.contact-row{display:flex;gap:14px;font-size:10.5px;line-height:18px;color:var(--muted);margin-bottom:10px}
.contact-row svg{flex:none;margin-top:2px}
.contact-row.strong{color:var(--blue);font-weight:600;font-size:13px}
</style>
</head>
<body>

<header class="site-header">
  <div class="brand" style="left:162px;top:24px">
    <span class="brand-mark"></span>
    <span class="brand-name">Bellcroft</span>
  </div>
  <nav class="main-nav">
    <span class="active">Home</span><span>About Us</span><span>Services</span><span>Gallery</span><span>Testimonials</span><span>Contact Us</span>
  </nav>
  <div class="btn phone-btn">
    <span class="ico"><svg width="14" height="14" viewBox="0 0 24 24"><path fill="#1a73c6" d="M6.6 10.8a15.1 15.1 0 0 0 6.6 6.6l2.2-2.2a1 1 0 0 1 1-.25 11.4 11.4 0 0 0 3.6.57 1 1 0 0 1 1 1V20a1 1 0 0 1-1 1A17 17 0 0 1 3 4a1 1 0 0 1 1-1h3.5a1 1 0 0 1 1 1c0 1.25.2 2.45.57 3.57a1 1 0 0 1-.25 1z"/></svg></span>
    123 456 7890
  </div>
</header>

<section>
  <div class="photo hero" role="img" aria-label="Modern luxury home lit up at night beside a pool"></div>
  <h1 class="abs hero-title">High End Luxury<br>Custom Home<br>Builder</h1>
  <div class="btn hero-btn">CONTACT US</div>
  <div class="abs hero-dots"><span></span><span></span><span></span><span style="background:#fff;box-shadow:0 0 0 3px #3d8fdc"></span></div>
</section>

<section>
  <div class="abs about"></div>
  <div class="photo about-photo" role="img" aria-label="Open glass living room and deck overlooking the sea and a pool"></div>
  <div class="abs about-card"></div>
  <h2 class="abs serif about-title">Bellcroft</h2>
  <div class="abs about-sub">CONSTRUCTION</div>
  <div class="abs about-text">
    <p>Lorem Ipsum is simply dummy text of the printing and typesetting industry. Lorem Ipsum has been the industry's standard dummy text ever since the 1500s, when an unknown printer.</p>
    <p>Lorem Ipsum is simply dummy text of the printing and typesetting industry. Lorem Ipsum has been the industry's standard dummy text ever since the 1500s, when an unknown printer took a galley of type and scrambled it to make a type specimen book.</p>
  </div>
  <div class="btn about-btn">LEARN MORE</div>
  <div class="abs play"><svg width="56" height="56" viewBox="0 0 56 56"><path d="M23 18v20l16-10z" fill="#1a73c6"/></svg></div>
</section>

<section>
  <p class="abs quote">Lorem Ipsum is simply dummy text of the printing and typesetting The industry. Lorem Ipsum has been the industry's standard dummy text ever since the 1500s, when an unknown printer.</p>
  <div class="abs quote-mark">”</div>
  <div class="abs client">– Client Name</div>
</section>

<section>
  <div class="abs services"></div>
  <h2 class="abs serif section-title" style="top:1654px">Services</h2>
  <div class="abs section-sub" style="top:1704px">What We Do</div>
  <div class="abs services-text">Lorem Ipsum is simply dummy text of the printing and typesetting industry.<br>Lorem Ipsum has been the industry's standard.<em>Lorem dummy text ever since the 1500s, when an unknown printer.</em></div>
  <div class="card" style="left:205px"><div class="img" role="img" aria-label="Builders in hard hats reviewing plans" style="background:linear-gradient(160deg,#eef2f6 0%,#d4dde6 45%,#8a96a2 75%,#3e4248 100%)"></div><h3>PLAN</h3><p>Lorem Ipsum is simply text</p><i></i></div>
  <div class="card featured" style="left:475px"><div class="img" role="img" aria-label="Architectural drawings with a tablet showing an interior" style="background:linear-gradient(160deg,#f7f7f5 0%,#e2e1dc 50%,#a9a7a0 80%,#5c5a55 100%)"></div><h3>DESIGN</h3><p>Lorem Ipsum is simply text</p><i></i></div>
  <div class="card" style="left:745px"><div class="img" role="img" aria-label="Completed villa with garden pond" style="background:linear-gradient(180deg,#cfe0f0 0%,#e6dccb 35%,#b59870 55%,#5d7a6a 78%,#3d4e3c 100%)"></div><h3>BUILD</h3><p>Lorem Ipsum is simply text</p><i></i></div>
</section>

<section>
  <h2 class="abs serif blog-title">Blog Post</h2>
  <div class="abs blog-sub">LOREM IPSUM IS SIMPLY DUMMY TEXT OF THE PRINTING &amp; TYPESETTING.</div>
  <p class="abs blog-text">Lorem Ipsum is simply dummy text of the printing and type setting industry. Lorem Ipsum has been the industry's thisis standard dummy text ever since the 1500s, when unknown printer Lorem Ipsum is simply dummy text.</p>
  <div class="btn blog-btn">LEARN MORE</div>
  <div class="photo blog-photo" role="img" aria-label="Two builders reviewing plans inside a home under construction"></div>
  <div class="abs arrows">
    <span><svg width="10" height="14" viewBox="0 0 10 14"><path d="M8 1 2 7l6 6" stroke="#fff" stroke-width="2" fill="none"/></svg></span>
    <span><svg width="10" height="14" viewBox="0 0 10 14"><path d="m2 1 6 6-6 6" stroke="#fff" stroke-width="2" fill="none"/></svg></span>
  </div>
</section>

<section>
  <h2 class="abs serif section-title" style="top:2824px">Gallery</h2>
  <div class="abs section-sub" style="top:2874px">Work Gallery</div>
  <div class="tile" style="left:0;top:2948px;width:503px;height:239px;background:linear-gradient(180deg,#e3ebf3,#a9bccf)" role="img" aria-label="Single storey home with pool"></div>
  <div class="abs tile-overlay"></div>
  <div class="abs tile-frame"></div>
  <svg class="abs" style="left:234px;top:3048px" width="38" height="38" viewBox="0 0 38 38"><circle cx="15" cy="15" r="11" stroke="#fff" stroke-width="2" fill="none"/><path d="M23 23l11 11" stroke="#fff" stroke-width="3"/><path d="M15 10v10M10 15h10" stroke="#fff" stroke-width="1.5"/></svg>
  <div class="abs tile-label">LOREM IPSUM</div>
  <div class="tile" style="left:513px;top:2948px;width:299px;height:239px;background:linear-gradient(180deg,#f4f4f2 0%,#dcdad5 45%,#8d8880 68%,#4a3526 100%)" role="img" aria-label="White kitchen with dark timber floor"></div>
  <div class="tile" style="left:821px;top:2948px;width:379px;height:320px;background:linear-gradient(180deg,#5f9fdc 0%,#a9cbeb 28%,#b86f45 48%,#8d6a52 62%,#b9b6ae 80%,#9a978f 100%)" role="img" aria-label="Two storey modern home with timber cladding"></div>
  <div class="tile" style="left:0;top:3195px;width:401px;height:241px;background:linear-gradient(180deg,#f6f6f4 0%,#e6e4df 60%,#c8a878 85%,#a98656 100%)" role="img" aria-label="White kitchen with open staircase"></div>
  <div class="tile" style="left:411px;top:3195px;width:401px;height:241px;background:linear-gradient(180deg,#f3f3f1 0%,#dddbd6 55%,#9c9994 80%,#4a4845 100%)" role="img" aria-label="Curved staircase in a white entry hall"></div>
  <div class="tile" style="left:821px;top:3278px;width:379px;height:158px;background:linear-gradient(180deg,#c5dcef 0%,#dfe9f0 30%,#6f8f6a 55%,#3da0c0 78%,#2a86a8 100%)" role="img" aria-label="Terrace with infinity pool overlooking the sea"></div>
  <div class="btn explore-btn">EXPLORE MORE</div>
</section>

<section>
  <div class="abs cta"></div>
  <div class="photo cta-house" role="img" aria-label="White two storey home with gardens"></div>
  <h2 class="abs cta-title">The Quality We<br>Provide</h2>
  <p class="abs cta-text">If you Have an any Question For Contact Us Today !</p>
  <div class="btn cta-btn">CONTACT US</div>
</section>

<footer>
  <div class="brand footer-brand">
    <span class="brand-mark" style="width:28px;height:28px"></span>
    <span class="brand-name" style="font-size:28px">Bellcroft</span>
  </div>
  <div class="abs socials"><span></span><span></span><span></span><span></span></div>
  <p class="abs copyright">©Bellcroft Construction - 2020 All rights reserved</p>

  <div class="f-col" style="left:403px"><h4>SITEMAP</h4><ul><li>Home</li><li>About Us</li><li>Services</li><li>Gallery</li><li>Testimonial</li><li>Contact Us</li></ul></div>
  <div class="f-col" style="left:553px"><h4>SERVICES</h4><ul><li>Plan</li><li>Design</li><li>Build</li></ul></div>
  <div class="f-col" style="left:695px"><h4>QUICKLINKS</h4><ul><li>Privacy Policy</li><li>Tearms &amp; Condition</li><li>Useful links</li></ul></div>
  <div class="f-col" style="left:870px"><h4>CONTACT US</h4>
    <div class="contact-row"><svg width="14" height="18" viewBox="0 0 14 18"><path d="M7 0a7 7 0 0 0-7 7c0 5 7 11 7 11s7-6 7-11a7 7 0 0 0-7-7zm0 10a3 3 0 1 1 0-6 3 3 0 0 1 0 6z" fill="#1a73c6"/></svg><span>Bellcroft Construction<br>101 - Lorem ipsum simple<br>print type setting text.</span></div>
    <div class="contact-row strong"><svg width="14" height="14" viewBox="0 0 24 24"><path fill="#1a73c6" d="M6.6 10.8a15.1 15.1 0 0 0 6.6 6.6l2.2-2.2a1 1 0 0 1 1-.25 11.4 11.4 0 0 0 3.6.57 1 1 0 0 1 1 1V20a1 1 0 0 1-1 1A17 17 0 0 1 3 4a1 1 0 0 1 1-1h3.5a1 1 0 0 1 1 1c0 1.25.2 2.45.57 3.57a1 1 0 0 1-.25 1z"/></svg><span>123 456 7890</span></div>
    <div class="contact-row" style="font-size:12px;color:#333"><svg width="15" height="12" viewBox="0 0 15 12"><rect width="15" height="12" rx="1" fill="#1a73c6"/><path d="m1 1 6.5 5L14 1" stroke="#fff" stroke-width="1.3" fill="none"/></svg><span>info@bellcroft.com</span></div>
  </div>
</footer>

</body>
</html>
```